Ski and Snowboard Instructor Business card

An eye catching business card capturing the essence of the sport and the mountain with a professional finish and easily readable contact information.

Notes on uploaded files:
I must have the KORV (Northern Guild of Alpine Coaching Tutors) Logo featured on the design (I designed it on the front but you can move if you think it would look better else where). The front of the card as you will see is a picture of a mountain top, if you can find a real image of this with a clear blue sky and snow that would be great -even better if it was from New Zealand as that is where I will be using the card!!! but also I am open to creative ones - logo style, 2D mountain outline etc.
As for the back something clean and simple, I originally designed it as matt black background with stylised writing for my name and a contrasting colour for the other writing. Possibly add the tag line 'certified snowsports instructor' I didn't just because of spacing etc but I'm keen to see what you guys come up with.

Writing on the back
Dana Whitcombe
SKI - SNOWBOARD
danawhitcombe2011@mailvale.example
NZ: 02109871536
UK: (+44) 07835216490
Hope this helps
Happy designing!

Industry/Entity Type

Business

Contact Information for Business Card

See description

Requirements
Must have
• KORV (Northern guild of Alpine Coaching Tutors) logo. It is a trademarked logo so please no alterations in shape or colour.
Nice to have
• Real Images of mountains, snow etc

```html
<!DOCTYPE html>
<html lang="en">
<head>
<meta charset="utf-8">
<title>Dana Whitcombe – Ski &amp; Snowboard Business Card</title>
<link rel="stylesheet" href="https://fonts.googleapis.com/css2?family=Parisienne&family=Questrial&family=Cinzel:wght@400&display=swap">
<style>
  :root {
    --backdrop: #8a8885;
    --sky-top: #2f6fb8;
    --sky-mid: #7fb0df;
    --sky-low: #c9dcef;
    --snow: #e9eef5;
    --rock: #2c3a58;
    --logo-blue: #1d3f8f;
    --logo-red: #d2232a;
    --name-light: #eef2f7;
    --card-black: #050505;
    --card-grey: #2a2a2a;
    --ink-white: #f4f4f4;
  }
  * { box-sizing: border-box; margin: 0; padding: 0; }
  html, body { width: 1200px; height: 871px; overflow: hidden; }
  body {
    background: var(--backdrop);
    display: flex;
    align-items: center;
    justify-content: center;
    gap: 40px;
  }
  .card {
    position: relative;
    width: 540px;
    height: 310px;
    overflow: hidden;
    box-shadow: 0 10px 28px rgba(0,0,0,.35);
  }

  /* Front */
  .card-front {
    background: linear-gradient(180deg, var(--sky-top) 0%, var(--sky-mid) 30%, var(--sky-low) 48%, var(--snow) 62%, #aab8cc 100%);
  }
  .front-scene {
    position: absolute;
    inset: 0;
    background:
      radial-gradient(ellipse 70% 38% at 62% 64%, rgba(44,58,88,.55), transparent 70%),
      linear-gradient(180deg, transparent 40%, rgba(233,238,245,.35) 70%, rgba(60,80,120,.35) 100%);
  }
  .front-logo {
    position: absolute;
    left: 28px;
    top: 36px;
    display: flex;
    align-items: center;
    gap: 10px;
  }
  .front-logo-mark {
    width: 30px;
    height: 30px;
    background: var(--logo-blue);
  }
  .front-logo-name {
    font-family: "Questrial", sans-serif;
    font-size: 40px;
    color: var(--logo-blue);
    letter-spacing: 1px;
    line-height: 1;
  }
  .front-name {
    position: absolute;
    left: 250px;
    top: 24px;
    font-family: "Parisienne", cursive;
    font-size: 48px;
    line-height: .95;
    color: var(--name-light);
    text-shadow: 0 0 2px rgba(60,70,90,.8), 1px 2px 3px rgba(0,0,0,.35);
  }
  .front-name span { display: block; }
  .front-name span + span { padding-left: 40px; }

  /* Back */
  .card-back {
    background: linear-gradient(100deg, var(--card-black) 0%, var(--card-black) 45%, var(--card-grey) 100%);
  }
  .back-scene {
    position: absolute;
    right: 0;
    top: 70px;
    width: 330px;
    height: 240px;
    background: radial-gradient(ellipse 70% 60% at 60% 55%, rgba(150,150,150,.28), rgba(40,40,40,0) 75%);
  }
  .back-content {
    position: absolute;
    left: 40px;
    top: 34px;
    color: var(--ink-white);
  }
  .back-name {
    font-family: "Parisienne", cursive;
    font-size: 38px;
    line-height: 1.1;
    margin-bottom: 4px;
  }
  .back-discipline {
    font-family: "Cinzel", serif;
    font-size: 14px;
    letter-spacing: 1px;
    margin-bottom: 28px;
  }
  .contact-list { list-style: none; }
  .contact-item {
    display: flex;
    align-items: center;
    gap: 16px;
    font-family: "Questrial", sans-serif;
    font-size: 15px;
    letter-spacing: .5px;
    margin-bottom: 14px;
  }
  .contact-icon { width: 20px; height: 16px; flex: none; }
</style>
</head>
<body>

  <section class="card card-front" aria-label="Card front">
    <div class="front-scene" role="img" aria-label="Snow-covered mountain summit under a clear blue sky"></div>
    <div class="front-logo">
      <span class="front-logo-mark"></span>
      <span class="front-logo-name">KORV</span>
    </div>
    <h1 class="front-name"><span>Dana</span><span>Whitcombe</span></h1>
  </section>

  <section class="card card-back" aria-label="Card back">
    <div class="back-scene" role="img" aria-label="Faint monochrome mountain range"></div>
    <div class="back-content">
      <h2 class="back-name">Dana Whitcombe</h2>
      <p class="back-discipline">SKI - SNOWBOARD</p>
      <ul class="contact-list">
        <li class="contact-item">
          <svg class="contact-icon" viewBox="0 0 20 16" aria-hidden="true"><rect x="1" y="2" width="18" height="12" fill="none" stroke="#f4f4f4" stroke-width="1.5"/><path d="M1 2 L10 9 L19 2" fill="none" stroke="#f4f4f4" stroke-width="1.5"/></svg>
          <span>danawhitcombe2011@mailvale.example</span>
        </li>
        <li class="contact-item">
          <svg class="contact-icon" viewBox="0 0 20 16" aria-hidden="true"><path d="M2 6 Q10 0 18 6 L15 8 L13 5 L7 5 L5 8 Z" fill="#f4f4f4"/><rect x="5" y="9" width="10" height="6" rx="1" fill="#f4f4f4"/></svg>
          <span>NZ: 02109871536</span>
        </li>
        <li class="contact-item">
          <svg class="contact-icon" viewBox="0 0 20 16" aria-hidden="true"><path d="M2 6 Q10 0 18 6 L15 8 L13 5 L7 5 L5 8 Z" fill="#f4f4f4"/><rect x="5" y="9" width="10" height="6" rx="1" fill="#f4f4f4"/></svg>
          <span>UK: (+44) 07835216490</span>
        </li>
      </ul>
    </div>
  </section>

</body>
</html>
```